Corporate services company needs a brochure

We are starting a company offering setup services to companies new to that location.
This includes services such as recruitment, company formation, advertising, marketing, pr, handling legal issues, logistics, transportation, procurement,immigration services, corporate gifts, accomodation,entertainment, training, administrative services etc.
Basically taking the setup issues off the hands of the company allowing them focus on their core business.

We are looking to design a professional brochure which would give the potential customers the confidence to entrust us with their needs.

We will be including some copy that can be used but i would very much like for you to bring what i have written to life - adding, deducting and amending where required.

We are looking at a A4 4/6 paged brochure but open to suggestions.

                                       

If you have any images that are suitable, please let us know. We will also be searching for some to add.

The first prize has been increased.

Thanks

Reason: We have just guaranteed the payment and we are hoping that this will encourage good designers to participate.

Reason: Some designers have requested more time to complete their final design.

Hi, I h extended the deadline to give designers more time to work on designs.

we are also looking at making the brochure a height of 8.5 and a width of 11. Please let me know your thoughts on this as any advice will help. The whole objective is to make it look as up to date and creative as possible. There is also another design size of 7.5 by 8.5

Thanks

                                        Hi

The copy has been revised and uploaded.

Hopefully it will give a clearer explanation of what we are trying to do.

Please let me know if you have any further questions.

Thanks

Marta

Reason: adding finishing touches to designs

Reason: We are amending the copy for the brochure

Reason: The new copy for the brochure is ready. I am sorry it has taken so long to get it out. I am sure we will not be making any amendments to it post today. Thanks for your patience The extension is not to attact new designs it is for existing designs's copy to be modified to include information from the updated copy.

Target Market(s)

medium to large companies in banking, telecom, retail etc. It will be viewed by middle and top management.

Industry/Entity Type

Legal

Requirements
Must have
• The brochure must clearly highlight all our services without just listing as this would risk it appearing as if we have just included everything we could think of!,
Please do not do the sitting round the conference table brochure or the typical blue and white brochure.
I desperately need it to be different, unique and serious enough to show that we are capable of handling/managing all what we have included.
Our clients include the many companies starting up an office in Africa.
We are anxious to have the potential clients understand that we will help them setup under any climax/
Nice to have
• modern colours but not too bright. there must still be a clear serious edge to it.
Should not have
• conference room table and people sitting around it.
the typical blue and white brochures often used for these type of services.

```html
<!DOCTYPE html>
<html lang="en">
<head>
<meta charset="utf-8">
<title>Travan brochure spread</title>
<link href="https://fonts.googleapis.com/css2?family=Open+Sans:wght@300;400;600;700&display=swap" rel="stylesheet">
<style>
  :root {
    --backdrop: #2a2a2c;
    --page-dark: #3b3e42;
    --page-dark-edge: #2f3235;
    --orange: #f29a1f;
    --orange-deep: #e38412;
    --text-light: #e6e6e6;
    --white: #ffffff;
    --sky-top: #6f9fcf;
    --sky-mid: #bcd3e6;
    --sand: #e8dccb;
  }
  * { box-sizing: border-box; margin: 0; padding: 0; }
  html, body { width: 1200px; height: 793px; overflow: hidden; }
  body {
    background: var(--backdrop);
    font-family: "Open Sans", Arial, sans-serif;
    position: relative;
  }
  .spread {
    position: absolute; left: 110px; top: 120px;
    width: 1030px; height: 560px;
    display: flex;
    box-shadow: 0 10px 30px rgba(0,0,0,.6);
  }
  .page { position: relative; height: 100%; overflow: hidden; }
  .page--left {
    width: 510px;
    background: linear-gradient(90deg, var(--page-dark) 0%, var(--page-dark) 88%, var(--page-dark-edge) 100%);
  }
  .page--right { width: 520px; }
  .bottom-band {
    position: absolute; left: 0; right: 0; bottom: 0; height: 16px;
    background: var(--orange);
  }
  .masthead {
    position: absolute; left: 14px; top: 42px; width: 480px; height: 78px;
    background: linear-gradient(90deg, var(--orange-deep), var(--orange));
    display: flex; align-items: center; padding: 0 12px;
  }
  .masthead__brand {
    width: 108px; display: flex; align-items: center; gap: 6px;
    color: var(--white); font-weight: 700; font-size: 22px;
  }
  .masthead__brand .dot { width: 10px; height: 10px; border-radius: 50%; background: var(--white); }
  .masthead__rule { width: 2px; height: 62px; background: var(--white); margin: 0 12px 0 6px; }
  .masthead__intro { color: var(--white); font-size: 8px; line-height: 10.5px; flex: 1; }
  .masthead__intro strong { font-size: 13px; font-weight: 700; margin-right: 4px; }
  .columns {
    position: absolute; left: 18px; top: 136px; right: 14px; bottom: 26px;
    display: flex; gap: 14px;
    color: var(--text-light); font-size: 7.6px; line-height: 10px;
  }
  .column { flex: 1; overflow: hidden; }
  .column h2 { font-size: 11px; font-weight: 700; color: var(--white); margin: 8px 0 2px; letter-spacing: .3px; }
  .column h3 { font-size: 8px; font-weight: 700; color: var(--white); margin-top: 6px; }
  .column p { margin-bottom: 3px; }
  .column ul { list-style: none; margin-bottom: 3px; }
  .column li::before { content: "• "; }
  .photo {
    position: absolute; inset: 0 0 16px 0;
    background: linear-gradient(180deg, var(--sky-top) 0%, var(--sky-mid) 48%, #d9e3ea 62%, var(--sand) 78%, #d8cab6 100%);
  }
  .headline {
    position: absolute; left: 28px; top: 44px; color: var(--white);
  }
  .headline__lead { font-weight: 700; font-size: 17px; letter-spacing: .3px; }
  .headline__sub { font-weight: 300; font-size: 15px; letter-spacing: .3px; }
  .brand-tag {
    position: absolute; right: 22px; bottom: 30px;
    color: var(--white); font-weight: 700; font-size: 18px; letter-spacing: .5px;
  }
</style>
</head>
<body>
  <main class="spread">
    <section class="page page--left">
      <header class="masthead">
        <div class="masthead__brand"><span class="dot"></span>Travan</div>
        <div class="masthead__rule"></div>
        <p class="masthead__intro"><strong>TRAVAN</strong> is a long established and multi-faceted organization dedicated to the provision of a wide range of professional services. Travan's years of experience in business solutions combined with a versatile group of professionals and an integration of multi-disciplinary approach broadens our capabilities and enhances our ability to identify, confront and resolve a variety of issues and concerns for clients across the world.</p>
      </header>
      <div class="columns">
        <div class="column">
          <h2>ABOUT US</h2>
          <p>"We are committed to providing excellence and inspiring confidence in everything we do. We are a dynamic and growing business, focused on meeting the changing needs of our clients.</p>
          <p>Our people are the secret to our success. By harnessing their expertise, we are consistently delivering value for our clients on projects around the world".</p>
          <p>Our focus at Travan is simple: It is to be the best in class consultant in all that we do. This success inspires confidence from our clients and pride from our people.</p>
          <p>We do it by respecting 3 fundamental values:</p>
          <ul>
            <li>Being imaginative in everything we do</li>
            <li>Being purposeful in everything we do</li>
            <li>Being dependable in everything we do</li>
          </ul>
          <p>That is why our message for clients, staff and partners is clear – 'TRAVAN, creative minds, and safe hands'.</p>
          <h2>WHAT WE DO</h2>
          <p>Here at Travan, we provide a diverse range of services to clients across numerous sectors worldwide, offering creative and effective solutions to their projects.</p>
          <p>Services – Travan offers clients a broad spread of high value services covering project management, cost consultancy. These skills are at the heart of decision making and are essential to the effective control of investment at all stages of the</p>
        </div>
        <div class="column">
          <p style="margin-top:8px">project cycle. Travan offers these services to leading multi-skilled teams.</p>
          <p>Office Setup<br>We offer expertise through the full lifecycle from concept feasibility and design services to contract preparation, site management, implementation and commissioning.</p>
          <p>We also cater for the design, procurement and management of public and private assets. These include:</p>
          <ul>
            <li>Office design and partition</li>
            <li>Renovation</li>
          </ul>
          <p>At Travan we align ourselves with a number of international real-estate brokers and professional services firms who specialize in introducing international corporate clients in Lagos. Though these alliances, we are able to support firms by offering additional benefits to their already long list of initiatives.</p>
          <p>Last Minute Catering and Corporate hospitality? Arranging local restaurants or simply ask us to serve gourmet meals directly in your meeting room.</p>
          <p style="margin-top:8px">If you are looking to setup a business in Lagos or rent an office in Lagos, Travan offers the services you need.</p>
          <p>Services:<br>Assisting with business incorporation.<br>Locating and providing Lagos office suites<br>Identifying and vetting appropriate local partners<br>Organizing work permits<br>Advising on suitable corporate structures.</p>
        </div>
        <div class="column">
          <p style="margin-top:8px">Relocation assisting (including shipping, culture training, sourcing domestic staff)</p>
          <p>Do you want to test the water before setting up a full fledge office?</p>
          <p>Want to grow without the costs?<br>Through Travan or via strategic partners we can offer:</p>
          <ul>
            <li>Business setup, incorporation and local JV and partnership services</li>
            <li>Warehousing, freight forwarding and logistic services.</li>
            <li>Call Centre and CRM Services.</li>
            <li>Accommodation, travel, car rental, hospitality and corporate entertainment.</li>
            <li>Account book keeping, recruitment, immigration etc.</li>
          </ul>
          <h3>COMPLIMENTARY SERVICES<br>YOUR LOCAL PARTNER FOR GROWTH</h3>
          <p>Travan can provide all the front and back office support your business needs to thrive in Lagos.</p>
          <p>From hotels to architects, companies in Lagos outsource the non-core parts of their business to Travan. Finding, quoting and comparing the services your company needs takes time and can slow you down. Let us do it for you!!!</p>
          <p>Travan – established and well-connected from accounting, marketing, and recruitment to real estate and storage, Travan either owns or are partners with businesses who can provide any of the additional jigsaw pieces you need to compliment your current business operations.</p>
        </div>
      </div>
      <div class="bottom-band"></div>
    </section>

    <section class="page page--right">
      <div class="photo" role="img" aria-label="Photo of a group of business people jumping with joy on a sunny beach under a blue sky, with a decorative overlay of translucent coloured circles near the headline"></div>
      <div class="headline">
        <p class="headline__lead">GETTING THE RIGHT ADVICE</p>
        <p class="headline__sub">CAN BE THE DIFFERENCE BETWEEN FAILURE AND SUCCESS</p>
      </div>
      <div class="brand-tag">TRAVAN</div>
      <div class="bottom-band"></div>
    </section>
  </main>
</body>
</html>
```